100% No Money Down

Flyer Design

Used for IG & FB (Social Media) Post. So avoid 8 1/2 x 11.

Target Market(s)

Real Estate Investors

Industry/Entity Type

Mortgage Brokerage

Requirements
Must have
• (LARGE BOLD FONT)
• 100% Investor Financing
• Fix & Flip Joint Ventures
• * Closing Costs Financed
• * 2-3 Week Close
• * No Score Minimum
• * No Reserve Requirement
• Contact: Marcus Delwyn
• Bluegate Lending Partners, Inc.
• NMLS #58307 / #916482
• Direct (240) 555-0193
• Email mdelwyn@bluegatelendpro.com

```html
<!DOCTYPE html>
<html lang="en">
<head>
<meta charset="utf-8">
<title>100% Investor Financing – Bluegate Lending Partners</title>
<link href="https://fonts.googleapis.com/css2?family=Oswald:wght@500;600&family=Lato:wght@400;700&display=swap" rel="stylesheet">
<style>
  :root {
    --blue: #1762aa;
    --gold: #ae9a2c;
    --sky: #c6ddef;
    --mist: #dde1e2;
    --white: #ffffff;
    --ink: #4a4d50;
    --photo-light: #e6ecea;
    --photo-mid: #b9c2c0;
    --photo-suit: #7f8684;
  }
  * { margin: 0; padding: 0; box-sizing: border-box; }
  html, body { width: 1200px; height: 1200px; overflow: hidden; background: var(--mist); }
  .flyer { position: relative; width: 1200px; height: 1200px; overflow: hidden; background: var(--mist); font-family: "Lato", sans-serif; }
  .hero-photo {
    position: absolute; left: 0; top: 0; width: 868px; height: 700px;
    background: radial-gradient(ellipse 55% 60% at 50% 62%, var(--photo-suit) 0%, var(--photo-mid) 55%, var(--photo-light) 100%);
  }
  .offer-panel { position: absolute; left: 868px; top: 0; width: 332px; height: 720px; background: var(--white); }
  .bands { position: absolute; inset: 0; }
  .brand { position: absolute; left: 868px; top: 96px; width: 332px; display: flex; flex-direction: column; align-items: center; gap: 12px; }
  .brand-dot { width: 46px; height: 46px; border-radius: 50%; background: var(--blue); }
  .brand-name { font-weight: 700; font-size: 21px; line-height: 1.2; color: var(--blue); text-align: center; }
  .offer-title { position: absolute; left: 868px; top: 238px; width: 332px; text-align: center; font-family: "Oswald", sans-serif; font-weight: 500; }
  .offer-percent { display: block; font-size: 110px; line-height: 110px; color: var(--gold); letter-spacing: -2px; }
  .offer-line { display: block; font-size: 64px; line-height: 82px; color: var(--blue); letter-spacing: -0.5px; }
  .headline { position: absolute; left: 29px; top: 598px; font-family: "Oswald", sans-serif; font-weight: 500; font-size: 62px; color: var(--white); letter-spacing: 0.5px; line-height: 1; }
  .features { position: absolute; left: 34px; top: 694px; list-style: none; color: var(--white); font-weight: 700; font-size: 36px; line-height: 42px; }
  .features li::before { content: "• "; }
  .portrait {
    position: absolute; left: 737px; top: 734px; width: 236px; height: 236px; border-radius: 50%;
    border: 8px solid var(--white); background: radial-gradient(circle at 50% 40%, #7d8fa6 0%, #3c4a5e 100%);
    box-shadow: 0 2px 8px rgba(0,0,0,0.2);
  }
  .contact { position: absolute; left: 577px; top: 915px; width: 623px; }
  .contact-label { font-family: "Oswald", sans-serif; font-weight: 600; font-size: 44px; color: var(--blue); line-height: 1; }
  .contact-rule { height: 5px; background: var(--sky); margin: 12px 0 12px; }
  .contact-name { font-family: "Oswald", sans-serif; font-weight: 500; font-size: 38px; color: var(--gold); line-height: 1; margin-bottom: 14px; }
  .contact-company { font-weight: 700; font-size: 25px; color: var(--ink); line-height: 28px; text-transform: uppercase; }
  .contact-line { font-size: 25px; color: var(--ink); line-height: 28px; position: relative; }
  .contact-icon { position: absolute; left: -34px; top: 4px; width: 24px; height: 22px; }
</style>
</head>
<body>
<main class="flyer">
  <div class="hero-photo" role="img" aria-label="Photo of a smiling investor in a grey suit with dollar bills falling around him"></div>
  <div class="offer-panel"></div>

  <svg class="bands" width="1200" height="1200" viewBox="0 0 1200 1200" aria-hidden="true">
    <polygon points="0,459 520,580 864,676 864,681 0,681" fill="var(--blue)"/>
    <polygon points="0,681 864,681 0,1055" fill="var(--gold)"/>
    <polygon points="0,1055 864,681 0,1200" fill="var(--sky)"/>
    <polygon points="0,1110 864,681 0,1200" fill="var(--mist)" opacity="0.55"/>
    <polygon points="1200,500 1200,537 864,681" fill="var(--sky)"/>
    <polygon points="1200,537 1200,681 864,681" fill="var(--gold)"/>
    <polygon points="864,681 1200,681 1200,800" fill="var(--blue)"/>
  </svg>

  <div class="brand">
    <span class="brand-dot"></span>
    <span class="brand-name">Bluegate Lending<br>Partners, Inc.</span>
  </div>

  <h1 class="offer-title">
    <span class="offer-percent">100%</span>
    <span class="offer-line">INVESTOR</span>
    <span class="offer-line">FINANCING</span>
  </h1>

  <h2 class="headline">FIX &amp; FLIP JOINT VENTURES</h2>
  <ul class="features">
    <li>Closing Costs Financed</li>
    <li>2-3 Week Closed</li>
    <li>No Reserve Requirement</li>
    <li>No Score Minimum</li>
  </ul>

  <div class="portrait" role="img" aria-label="Headshot portrait of Marcus Delwyn"></div>

  <section class="contact">
    <div class="contact-label">CONTACT:</div>
    <div class="contact-rule"></div>
    <div class="contact-name">MARCUS DELWYN</div>
    <div class="contact-company">Bluegate Lending Partners, Inc.</div>
    <div class="contact-line">NMLS #58307 / #916482</div>
    <div class="contact-line">
      <svg class="contact-icon" viewBox="0 0 24 24" aria-hidden="true"><path fill="var(--gold)" d="M6.6 10.8a15.1 15.1 0 0 0 6.6 6.6l2.2-2.2c.3-.3.7-.4 1-.2 1.1.4 2.3.6 3.6.6.6 0 1 .4 1 1V20c0 .6-.4 1-1 1A17 17 0 0 1 3 4c0-.6.4-1 1-1h3.5c.6 0 1 .4 1 1 0 1.3.2 2.5.6 3.6.1.3 0 .7-.2 1z"/></svg>
      Direct (240) 555-0193
    </div>
    <div class="contact-line">
      <svg class="contact-icon" viewBox="0 0 24 20" aria-hidden="true"><rect x="1.5" y="3" width="21" height="14" fill="none" stroke="var(--gold)" stroke-width="2"/><path d="M1.5 3l10.5 8 10.5-8" fill="none" stroke="var(--gold)" stroke-width="2"/></svg>
      mdelwyn@bluegatelendpro.com
    </div>
  </section>
</main>
</body>
</html>
```